Info about Getting Rid of Items That People No Longer Want or Need and Would Rather Have the Cash

We need a flyer made to pass out to potential customers describing what it is that we do. We would like for it to be a one page front and back flyer.
Our company helps people who are downsizing or getting rid of items that they no longer want and are unsure of their value. Most Millennials have no interest in their parents items--whether that be art, sterling flatware, jewelry, decorative items or collectibles. On top of that the market is slowing turning as there is more 'stuff" on the market than ever before and less buyers.
We have included some images as examples. For instance: a newspaper headline showing "Millennials Don't Want Your Stuff". In one of the small columns below there could be a picture of an Felix Dunmore painting with a caption reading "Man Buys Original Dunmore for $20 in Garage Sale". Or something like that.
We are open to suggestions and encourage your creativity. These are just examples of what we came up with. These issues, kids not wanting their parents stuff and worry about squandering something special because they didn't know what it is and what its worth are big concerns.
On the back page we are thinking about using a 5 step process to simplify what we do.
Below is a rough example of the 5 steps.
1) Schedule Free In-Home Visit
Please contact us to schedule an appointment
2) Questions, Answers and Facts
We will answer any questions you have and ask you enough questions to make sure we know what your goals are. We will also inform you about market trends and other information related to downsizing
3) The Tour and The Treasure Hunt
You will take us on a tour of your home and point out items you are selling. We will take pictures, notes and point out any treasures that you may not realize you have.
4) Research, Research, Research
We take our notes and photographs back to research your items. Then we will check with our network of experts, dealers and buyers across the country to determine the best market.
5) The Game Plan
We will go over our findings with you. Then we will discuss ways to sell the items to get the highest return.
We have also attached sample images of our business card. We will also want to include our contact information:
Gordon Pellham
555-382-9170
info@gordonapellham.example
www.gordonapellham.example
Target Market(s)
Elderly People or people downsizing
Industry/Entity Type
Cash
Font styles to use
Colors
Designer to choose colors to be used in the design.
Look and feel

```html
<!DOCTYPE html>
<html lang="en">
<head>
<meta charset="utf-8">
<title>Gordon A Pellham – Collectible Asset Flyer</title>
<link href="https://fonts.googleapis.com/css2?family=Raleway:wght@400;500;600;700;800&family=Oswald:wght@700&family=Playfair+Display:wght@900&display=swap" rel="stylesheet">
<style>
  :root{
    --gold:#b08a3e;
    --gold-deep:#8e6c2a;
    --brown-dark:#2a1a12;
    --ink:#2b2b2b;
    --step-grey:#dcdcdc;
    --paper:#e9e7e2;
    --stage:#5b5b5b;
    --white:#ffffff;
  }
  *{box-sizing:border-box;margin:0;padding:0}
  html,body{width:1200px;height:1200px;overflow:hidden}
  body{background:var(--stage);font-family:"Raleway",sans-serif;position:relative;font-variant-numeric:lining-nums;font-feature-settings:"lnum" 1}
  .page{position:absolute;top:221px;width:536px;height:758px;background:var(--white);overflow:hidden}
  .page--front{left:63px}
  .page--back{left:602px}
  .abs{position:absolute}

  /* front */
  .hero-photo{left:0;top:0;width:536px;height:394px;
    background:linear-gradient(135deg,#5a3418 0%,#7a4a22 40%,#4a2a14 75%,#2e1a0e 100%)}
  .name-band{left:161px;top:199px;width:375px;height:92px;background:var(--gold);
    text-align:right;padding:10px 31px 0 0}
  .name-band__name{color:var(--white);font-weight:700;font-size:32px;line-height:34px;letter-spacing:-.3px}
  .name-band__role{color:var(--brown-dark);font-weight:400;font-size:18px;line-height:20px}
  .story-band{left:0;top:394px;width:536px;height:141px;background:var(--brown-dark)}
  .story-headline{left:31px;top:33px;width:300px;white-space:nowrap;color:var(--gold);font-weight:400;font-size:26px;line-height:31px;letter-spacing:0}
  .story-headline b{font-weight:700}
  .painting{left:337px;top:345px;width:174px;height:201px;
    background:linear-gradient(135deg,#c9a04a,#8a6420);padding:17px 16px}
  .painting__canvas{width:100%;height:100%;background:linear-gradient(160deg,#3ec6c0 0%,#e8d84a 35%,#e99aa8 65%,#3ec6c0 100%)}
  .intro{left:31px;top:558px;width:474px;font-size:13.2px;line-height:19.2px;color:var(--ink);text-align:justify}

  /* footer shared */
  .footer{left:0;top:0;width:536px;height:758px;pointer-events:none}
  .footer-cta{left:31px;top:694px;color:var(--white);font-size:14px}
  .footer-cta b{font-weight:800}
  .footer-name{left:31px;top:712px;color:var(--gold);font-weight:700;font-size:21px;letter-spacing:-.2px}
  .contact{left:306px;top:677px;width:222px;list-style:none;color:var(--white);font-size:13px;line-height:18.5px;white-space:nowrap}
  .contact li{display:flex;align-items:center;gap:6px}
  .contact .phone{font-weight:700;font-size:14.5px}
  .contact svg{width:12px;height:12px;flex:none}

  /* back */
  .desk-photo{left:0;top:0;width:536px;height:758px;
    background:linear-gradient(180deg,#6b4828 0%,#8a6038 30%,#6e4a2a 55%,#c9c6c1 62%,#d7d5d2 100%)}
  .newspaper{left:36px;top:0;width:480px;height:240px;background:var(--paper)}
  .masthead{left:0;top:22px;width:480px;text-align:center;font-family:"Playfair Display",serif;font-weight:900;font-size:40px;color:#1d1d1d;letter-spacing:-1px}
  .paper-rule{left:20px;top:10px;width:440px;height:5px;background:#2a2a2a}
  .dateline{left:20px;top:78px;width:440px;height:18px;border-top:1px solid #333;border-bottom:1px solid #333;
    display:flex;justify-content:space-between;align-items:center;padding:0 6px;font-weight:700;font-size:9px;color:#222}
  .paper-headline{left:0;top:104px;width:480px;text-align:center;font-family:"Oswald",sans-serif;font-weight:700;font-size:52px;line-height:52px;color:#1f1f1f;letter-spacing:-.5px}
  .paper-sub{left:40px;top:218px;width:420px;display:flex;justify-content:flex-end;gap:18px;font-weight:700;font-size:9px;color:#333}
  .steps-panel{left:32px;top:229px;width:472px;height:430px;background:var(--white)}
  .step{position:absolute;left:130px;width:374px;background:var(--step-grey);padding:8px 14px 0 16px}
  .step::before{content:"";position:absolute;left:-12px;top:12px;border:12px solid transparent;border-right-color:var(--step-grey);border-left:0}
  .step__title{color:var(--gold);font-weight:700;font-size:14.5px;line-height:17px}
  .step__text{color:var(--ink);font-size:12px;line-height:15.2px;text-align:justify}
  .step-num{position:absolute;left:16px;width:32px;height:32px;background:var(--gold);color:var(--white);
    font-weight:700;font-size:24px;line-height:32px;text-align:center}
  .step-num::after{content:"";position:absolute;left:0;top:32px;border-top:8px solid var(--brown-dark);border-left:8px solid transparent}
  .step-icon{position:absolute;left:54px;width:56px;height:56px}
</style>
</head>
<body>

<!-- FRONT -->
<section class="page page--front">
  <div class="abs hero-photo" role="img" aria-label="Photo of the consultant standing with arms crossed in front of wooden bookshelves"></div>
  <div class="abs name-band">
    <div class="name-band__name">GORDON A PELLHAM</div>
    <div class="name-band__role">COLLECTIBLE ASSET BUYER</div>
    <div class="name-band__role">BROKER &amp; CONSULTANT</div>
  </div>
  <div class="abs story-band">
    <h1 class="abs story-headline">MAN BUYS ORIGINAL<br>DUNMORE FOR <b>$20</b> IN<br>GARAGE SALE</h1>
  </div>
  <svg class="abs" style="left:0;top:528px" width="536" height="30" viewBox="0 0 536 30">
    <polygon points="0,0 370,0 340,7 0,7" fill="#2a1a12"/>
  </svg>
  <div class="abs painting" role="img" aria-label="Ornate gilt frame holding a bright pop-art portrait painting">
    <div class="painting__canvas"></div>
  </div>
  <p class="abs intro">Our company helps people who are downsizing or getting rid of items that they no longer want and are unsure of their value. Most Millennials have no interest in their parents items--whether that be art, sterling flatware, jewelry, decorative items or collectibles. On top of that the market is slowing turning as there is more ‘stuff” on the market than ever before and less buyers.</p>

  <svg class="abs footer" viewBox="0 0 536 758">
    <rect x="0" y="686" width="536" height="72" fill="#2a1a12"/>
    <polygon points="281,659 536,659 536,758 247,758" fill="#b08a3e"/>
  </svg>
  <p class="abs footer-cta">Call For a <b>FREE</b> Consultation</p>
  <p class="abs footer-name">GORDON A PELLHAM</p>
  <ul class="abs contact">
    <li class="phone"><svg viewBox="0 0 12 12"><circle cx="6" cy="6" r="5.3" fill="none" stroke="#fff"/><path d="M4 3.3l1 1.2-.6.8c.4.8 1 1.4 1.8 1.8l.8-.6 1.2 1-.6 1c-2.3-.3-4-2-4.3-4.3z" fill="#fff"/></svg>555-382-9170</li>
    <li><svg viewBox="0 0 12 12"><circle cx="6" cy="6" r="5.3" fill="none" stroke="#fff"/><rect x="3.2" y="4" width="5.6" height="4" fill="none" stroke="#fff" stroke-width=".8"/><path d="M3.2 4l2.8 2.2L8.8 4" fill="none" stroke="#fff" stroke-width=".8"/></svg>info@gordonapellham.example</li>
    <li><svg viewBox="0 0 12 12"><circle cx="6" cy="6" r="5.3" fill="none" stroke="#fff"/><path d="M4.5 3.5l4 2.3-1.8.5.9 1.8-.7.3-.9-1.8-1.3 1.2z" fill="#fff"/></svg>www.gordonapellham.example</li>
  </ul>
</section>

<!-- BACK -->
<section class="page page--back">
  <div class="abs desk-photo" role="img" aria-label="Photo of a folded newspaper lying on a wooden desk"></div>
  <div class="abs newspaper">
    <div class="abs paper-rule"></div>
    <div class="abs masthead">THE DAILY LEDGER</div>
    <div class="abs dateline"><span>Since 1883</span><span>YOUR NUMBER ONE SOURCE FOR HEADLINES</span><span>$1.00</span></div>
    <h2 class="abs paper-headline">MILLENNIALS DON’T<br>WANT YOUR STUFF</h2>
    <div class="abs paper-sub"><span>COST AND IMPACT OF</span><span>“A WEIGHTY ISSUE” AS</span></div>
  </div>

  <div class="abs steps-panel"></div>

  <div class="step" style="top:241px;height:48px">
    <h3 class="step__title">Schedule Free In-Home Visit</h3>
    <p class="step__text">Please contact us to schedule an appointment</p>
  </div>
  <div class="step" style="top:297px;height:99px">
    <h3 class="step__title">Questions, Answers and Facts</h3>
    <p class="step__text">We will answer any questions you have and ask you enough questions to make sure we know what your goals are. We will also inform you about market trends and other information related to downsizing</p>
  </div>
  <div class="step" style="top:406px;height:79px">
    <h3 class="step__title">The Tour and The Treasure Hunt</h3>
    <p class="step__text">You will take us on a tour of your home and point out items you are selling. We will take pictures, notes and point out any treasures that you may not realize you have.</p>
  </div>
  <div class="step" style="top:494px;height:79px">
    <h3 class="step__title">Research, Research, Research</h3>
    <p class="step__text">We take our notes and photographs back to research your items. Then we will check with our network of experts, dealers and buyers across the country to determine the best market.</p>
  </div>
  <div class="step" style="top:582px;height:68px">
    <h3 class="step__title">The Game Plan</h3>
    <p class="step__text">We will go over our findings with you. Then we will discuss ways to sell the items to get the highest return.</p>
  </div>

  <div class="step-num" style="top:247px">1</div>
  <div class="step-num" style="top:318px">2</div>
  <div class="step-num" style="top:426px">3</div>
  <div class="step-num" style="top:509px">4</div>
  <div class="step-num" style="top:601px">5</div>

  <svg class="step-icon" style="top:232px" viewBox="0 0 56 56" fill="none" stroke="#b08a3e" stroke-width="3">
    <rect x="3" y="8" width="38" height="34" rx="2"/><line x1="3" y1="17" x2="41" y2="17"/>
    <line x1="12" y1="3" x2="12" y2="11"/><line x1="32" y1="3" x2="32" y2="11"/>
    <path d="M10 24h6M20 24h6M10 32h6M20 32h6"/>
    <circle cx="41" cy="42" r="11" fill="#fff"/><path d="M41 36v12M35 42h12"/>
  </svg>
  <svg class="step-icon" style="top:308px" viewBox="0 0 56 56" fill="none" stroke="#b08a3e" stroke-width="3">
    <path d="M4 16a14 12 0 1 1 8 11l-6 4 2-6a12 12 0 0 1-4-9z"/>
    <path d="M52 36a13 11 0 1 0-8 10l6 4-2-6a11 11 0 0 0 4-8z" fill="#fff"/>
    <text x="12" y="22" font-family="Raleway,sans-serif" font-weight="700" font-size="15" fill="#b08a3e" stroke="none">Q</text>
    <text x="34" y="42" font-family="Raleway,sans-serif" font-weight="700" font-size="14" fill="#b08a3e" stroke="none">A</text>
  </svg>
  <svg class="step-icon" style="top:415px" viewBox="0 0 56 56">
    <path d="M2 10l16-6 18 6 18-6v40l-18 6-18-6-16 6z" fill="#b08a3e"/>
    <path d="M9 32c5-10 10 2 16-6s9 4 14 0" fill="none" stroke="#fff" stroke-width="2" stroke-dasharray="3 3"/>
    <path d="M40 14l6 6M46 14l-6 6" stroke="#fff" stroke-width="2.5"/>
  </svg>
  <svg class="step-icon" style="top:497px" viewBox="0 0 56 56" fill="none" stroke="#b08a3e" stroke-width="3">
    <path d="M18 6h22l12 12v36H18z" fill="#fff"/><path d="M40 6v12h12"/>
    <path d="M25 32h20M25 40h20M25 48h20"/>
    <circle cx="14" cy="15" r="8" fill="#fff"/><line x1="8" y1="21" x2="2" y2="27"/>
  </svg>
  <svg class="step-icon" style="top:588px" viewBox="0 0 56 56" fill="none" stroke="#b08a3e" stroke-width="3">
    <path d="M10 2h26l12 12v40H10z"/><path d="M36 2v12h12"/>
    <rect x="30" y="20" width="8" height="8"/><path d="M20 24h10M20 24v10"/>
    <circle cx="20" cy="42" r="4"/><path d="M26 42h6"/><path d="M38 37l5 9h-10z"/>
  </svg>

  <svg class="abs footer" viewBox="0 0 536 758">
    <rect x="0" y="686" width="536" height="72" fill="#2a1a12"/>
    <polygon points="281,659 536,659 536,758 247,758" fill="#b08a3e"/>
  </svg>
  <p class="abs footer-cta">Call For a <b>FREE</b> Consultation</p>
  <p class="abs footer-name">GORDON A PELLHAM</p>
  <ul class="abs contact">
    <li class="phone"><svg viewBox="0 0 12 12"><circle cx="6" cy="6" r="5.3" fill="none" stroke="#fff"/><path d="M4 3.3l1 1.2-.6.8c.4.8 1 1.4 1.8 1.8l.8-.6 1.2 1-.6 1c-2.3-.3-4-2-4.3-4.3z" fill="#fff"/></svg>555-382-9170</li>
    <li><svg viewBox="0 0 12 12"><circle cx="6" cy="6" r="5.3" fill="none" stroke="#fff"/><rect x="3.2" y="4" width="5.6" height="4" fill="none" stroke="#fff" stroke-width=".8"/><path d="M3.2 4l2.8 2.2L8.8 4" fill="none" stroke="#fff" stroke-width=".8"/></svg>info@gordonapellham.example</li>
    <li><svg viewBox="0 0 12 12"><circle cx="6" cy="6" r="5.3" fill="none" stroke="#fff"/><path d="M4.5 3.5l4 2.3-1.8.5.9 1.8-.7.3-.9-1.8-1.3 1.2z" fill="#fff"/></svg>www.gordonapellham.example</li>
  </ul>
</section>

</body>
</html>
```